New Brochures to deliver confidence of our company to our customers

I would like to have new brochure to be used to distribute to our prospective customers besides the power point presentation. I like the powerpoint you did for us and would like to follow the direction that you have set up. I will attach a number of photos for you to include in our brochure for you to choose. I like the brochure to be modern and forward thinking but just practical. The brochure needs to have three languages which are English, Chinese and Japanese. Attaches is the power point that we like.

Target Market(s)

Multinational companies

Industry/Entity Type

Electronics

Colors

Designer to choose colors to be used in the design.

Requirements
Must have
• Feel lively and modern and yet giving people a sense of confidence. Highlighting the automation is important. Can let us know if you want more photos. The brochure will have three languages, namely english, japanese and chinese.

```html
<!DOCTYPE html>
<html lang="en">
<head>
<meta charset="utf-8">
<title>Norvale International Limited – Brochure</title>
<link href="https://fonts.googleapis.com/css2?family=Open+Sans:wght@400;600;700&family=Roboto+Condensed:wght@400;700&display=swap" rel="stylesheet">
<style>
:root{
  --bg:#8a8a8a;
  --paper:#ffffff;
  --green:#3fa84d;
  --green-mid:#7cc489;
  --green-light:#b9dfc1;
  --green-pale:#d8eedc;
  --green-dark:#2d6b39;
  --ink:#3a3a3a;
  --ink-soft:#6a6a6a;
  --photo-a:#9aa3a2;
  --photo-b:#c9cfcd;
}
*{margin:0;padding:0;box-sizing:border-box}
html,body{width:1200px;height:1200px;overflow:hidden}
body{background:var(--bg);font-family:"Open Sans",Arial,sans-serif;color:var(--ink);position:relative}
.spread{position:absolute;left:200px;width:800px;height:540px;display:flex;box-shadow:0 6px 18px rgba(0,0,0,.3)}
.spread--cover{top:40px}
.spread--inside{top:620px}
.page{position:relative;width:400px;height:540px;background:var(--paper);overflow:hidden}
.page--left{border-right:1px solid #e3e3e3}
.heading{font-family:"Roboto Condensed",Arial,sans-serif;color:var(--green-dark);text-transform:uppercase;font-weight:400}
.photo{background:linear-gradient(135deg,var(--photo-b),var(--photo-a))}

/* back cover */
.customers{position:absolute;left:26px;top:40px;width:348px;height:270px;border:1px solid var(--green)}
.customers__title{position:absolute;left:14px;top:-12px;background:var(--paper);padding:0 6px;font-size:19px}
.customers__intro{position:absolute;left:20px;top:18px;width:310px;font-size:8.5px;line-height:1.45;color:var(--ink-soft)}
.badges{position:absolute;left:20px;top:62px;width:310px;display:grid;grid-template-columns:repeat(5,1fr);gap:9px}
.badge{height:30px;border:1px solid #dcdcdc;border-radius:5px;background:#fafafa;display:flex;align-items:center;justify-content:center}
.badge span{display:block;width:34px;height:10px;border-radius:2px;background:#e2e2e2}
.back-band{position:absolute;left:0;top:335px;width:400px;height:205px;background:var(--green-light)}
.back-band__name{position:absolute;right:30px;top:38px;font-size:19px;letter-spacing:1px;color:var(--green-dark)}
.back-band__visit{position:absolute;right:30px;top:100px;text-align:right;font-size:17px;letter-spacing:2px;color:var(--green-dark);font-family:"Roboto Condensed",Arial,sans-serif}
.back-band__stripes{position:absolute;left:0;bottom:0}

/* front cover */
.front-frame{position:absolute;inset:16px;border:1px solid var(--green-dark)}
.front-brand{position:absolute;left:0;right:0;top:120px;text-align:center}
.front-brand__mark{font-family:"Roboto Condensed",Arial,sans-serif;font-weight:700;font-size:54px;letter-spacing:6px;color:var(--green-dark)}
.front-brand__tag{font-size:8px;letter-spacing:2px;color:var(--ink-soft);text-transform:uppercase;border-top:1px solid var(--green-dark);display:inline-block;padding-top:4px;margin-top:2px}
.front-brand__name{font-size:17px;letter-spacing:1px;margin-top:12px}
.front-art{position:absolute;left:0;top:260px}

/* inside left */
.bg-title{position:absolute;left:22px;top:28px;font-size:22px;font-weight:700}
.bg-rule{position:absolute;left:22px;top:60px;width:356px;height:1px;background:var(--green)}
.bg-text{position:absolute;left:22px;top:72px;width:168px;font-size:8.4px;line-height:1.4;text-align:justify;color:var(--ink)}
.bg-text p{margin-bottom:6px}
.bg-photo-top{position:absolute;left:202px;top:72px;width:176px;height:110px}
.invest{position:absolute;left:202px;top:192px;width:198px;height:300px;background:var(--green);color:#fff;padding:14px 16px}
.invest__title{font-family:"Roboto Condensed",Arial,sans-serif;font-size:19px;line-height:1.1;text-transform:uppercase;margin-bottom:10px}
.invest__text{font-size:8.4px;line-height:1.42;text-align:justify}
.invest__text p{margin-bottom:6px}
.bg-photo-bottom{position:absolute;left:0;top:345px;width:202px;height:195px}

/* inside right */
.single-title{position:absolute;left:22px;top:26px;font-size:17px;font-weight:700}
.single-rule{position:absolute;left:22px;top:50px;width:356px;height:1px;background:var(--green)}
.single-intro{position:absolute;left:22px;top:58px;width:210px;font-size:8.4px;line-height:1.4;color:var(--ink-soft)}
.apps{position:absolute;left:22px;top:102px;width:210px;border-collapse:collapse;font-size:8.6px}
.apps th{font-weight:600;text-align:left;padding:3px 4px;background:#eeeeee;color:var(--ink)}
.apps th:last-child,.apps td:last-child{text-align:right}
.apps td{padding:3px 4px;color:var(--ink-soft)}
.single-photo{position:absolute;left:244px;top:62px;width:134px;height:100px}
.facility-title{position:absolute;left:22px;top:200px;width:140px;font-size:11px;line-height:1.2;font-weight:700}
.facility-photos{position:absolute;left:22px;top:232px;width:140px;display:flex;flex-direction:column;gap:8px}
.facility-photos .photo{height:86px}
.double{position:absolute;left:176px;top:200px;width:202px}
.double__title{font-size:11px;font-weight:700;line-height:1.2;margin-bottom:8px}
.double__text{font-size:8.2px;line-height:1.42;color:var(--ink)}
.double__text p{margin-bottom:6px}
.right-corner{position:absolute;right:0;bottom:0}
</style>
</head>
<body>

<section class="spread spread--cover">
  <article class="page page--left back-cover">
    <div class="customers">
      <h2 class="heading customers__title">Customers</h2>
      <p class="customers__intro">Norvale is embracing a philosophy of being a partner with our customers. As a result, we are strategic PCB suppliers to the following world renowned companies:</p>
      <div class="badges" aria-label="Customer badges">
        <div class="badge"><span></span></div><div class="badge"><span></span></div><div class="badge"><span></span></div><div class="badge"><span></span></div><div class="badge"><span></span></div>
        <div class="badge"><span></span></div><div class="badge"><span></span></div><div class="badge"><span></span></div><div class="badge"><span></span></div><div class="badge"><span></span></div>
        <div class="badge"><span></span></div><div class="badge"><span></span></div><div class="badge"><span></span></div><div class="badge"><span></span></div><div class="badge"><span></span></div>
        <div class="badge"><span></span></div><div class="badge"><span></span></div><div class="badge"><span></span></div><div class="badge"><span></span></div><div class="badge"><span></span></div>
        <div class="badge"><span></span></div><div class="badge"><span></span></div>
      </div>
    </div>
    <div class="back-band">
      <p class="heading back-band__name">Norvale International Limited</p>
      <p class="back-band__visit">Visit Us<br>www.norvale-pcb.com</p>
      <svg class="back-band__stripes" width="400" height="205" viewBox="0 0 400 205">
        <polygon points="0,60 290,205 0,205" fill="#ffffff" opacity=".35"/>
        <polygon points="0,100 210,205 0,205" fill="#ffffff" opacity=".35"/>
        <polygon points="0,140 130,205 0,205" fill="var(--green-mid)" opacity=".6"/>
      </svg>
    </div>
  </article>

  <article class="page page--right front-cover">
    <div class="front-frame"></div>
    <div class="front-brand">
      <div class="front-brand__mark">NORVALE</div>
      <div class="front-brand__tag">Circuit Boards Built Right</div>
      <p class="heading front-brand__name">Norvale International Limited</p>
    </div>
    <svg class="front-art" width="400" height="200" viewBox="0 0 400 200">
      <path d="M0,20 Q200,-10 400,0 L400,180 Q200,190 0,150 Z" fill="var(--green-light)"/>
      <path d="M0,50 Q200,20 400,30 L400,150 Q200,165 0,130 Z" fill="var(--photo-a)" role="img" aria-label="Photo of automated PCB production machines on the factory floor"/>
      <polygon points="230,150 400,0 400,150" fill="var(--green)" opacity=".85"/>
      <polygon points="300,150 400,50 400,150" fill="var(--green-mid)" opacity=".8"/>
      <path d="M0,150 Q200,190 400,180" stroke="var(--green-dark)" stroke-width="1" fill="none"/>
    </svg>
  </article>
</section>

<section class="spread spread--inside">
  <article class="page page--left background-page">
    <h2 class="heading bg-title">Norvale Background</h2>
    <div class="bg-rule"></div>
    <div class="bg-text">
      <p>Established in 2007, Norvale International Limited is a Hong Kong company specializing in single and double sided printed circuit boards.</p>
      <p>Its manufacturing facility is located in a self-owned facility in China which is 50 minutes from Hong Kong.</p>
      <p>Our mission is to become a premium low costs PCB supplier that fully embraces human, social and environmental responsibilities.</p>
      <p>Through our insatiable drive to maximize efficiency, Norvale is becoming a highly efficient PCB factory with a capacity of 140,000 sq meter a month.</p>
      <p>PCB is our business and it is through continued automation and innovation that will drive our growth in the next 10 years.</p>
    </div>
    <div class="photo bg-photo-top" role="img" aria-label="Photo of an automated conveyor line in a clean production hall"></div>
    <div class="photo bg-photo-bottom" role="img" aria-label="Photo of PCB processing machines and stacked board panels on pallets"></div>
    <div class="invest">
      <h3 class="invest__title">Our Investment<br>and Upgrade</h3>
      <div class="invest__text">
        <p>Maintaining a highly automated factory is the only way to ensure consistent product and long term competitive efficiency.</p>
        <p>From 2015 to 2017, Norvale invested over US$3.5 million in automating our production and quality control process and enhancing our environmental processing facility.</p>
        <p>We will spend a further US$1.5 million in 2018 to continue our improvement process to ensure we are one of the most efficient and highest quality single sided PCB manufacturers in Asia.</p>
        <p>By the end of 2018, 100% of our PCBs will be inspected by AVI before they are delivered to our customers.</p>
      </div>
    </div>
  </article>

  <article class="page page--right boards-page">
    <h2 class="heading single-title">Single Layered Printed Circuit Boards</h2>
    <div class="single-rule"></div>
    <p class="single-intro">We are offering single layered circuit boards through our own production facility in China for customers in the following industries:</p>
    <table class="apps">
      <thead><tr><th>Application</th><th>比例 %</th></tr></thead>
      <tbody>
        <tr><td>Household appliances</td><td>60%</td></tr>
        <tr><td>Power supply</td><td>20%</td></tr>
        <tr><td>Lighting control system</td><td>10%</td></tr>
        <tr><td>Others</td><td>10%</td></tr>
      </tbody>
    </table>
    <div class="photo single-photo" role="img" aria-label="Photo of an automatic inspection machine"></div>
    <h3 class="heading facility-title">Show Pictures of<br>the Facility</h3>
    <div class="facility-photos">
      <div class="photo" role="img" aria-label="Photo of a drilling machine bed"></div>
      <div class="photo" role="img" aria-label="Photo of a board transfer line"></div>
      <div class="photo" role="img" aria-label="Photo of a plating line"></div>
    </div>
    <div class="double">
      <h3 class="heading double__title">Double Layered and Multi-Layered Printed Circuit Boards</h3>
      <div class="double__text">
        <p>We are offering two layered and multi-layered circuit boards for our customers through our strategically approved printed circuit boards manufacturers.</p>
        <p>With our own UL for double sided and multi-layered circuit boards, we work with a number of strategically approved manufacturers in delivering 100% quality guaranteed printed circuit boards for our customers.</p>
        <p>All the PCBs are inspected by our own Automatic Visual Inspection (AVI) Machine before we deliver to customers.</p>
        <p>We perform comprehensive quality and environmental audit of our manufacturers on quarterly and annual basis.</p>
      </div>
    </div>
    <svg class="right-corner" width="140" height="130" viewBox="0 0 140 130">
      <polygon points="0,130 140,0 140,130" fill="var(--green)"/>
      <polygon points="60,130 140,60 140,130" fill="var(--green-mid)" opacity=".7"/>
    </svg>
  </article>
</section>

</body>
</html>
```